Used Car Business Card Design

Maple Ridge Auto Sales is a woman owned women friendly car lot.  We focus on providing Professionalism, Integrity and Respect beginning with the initial introduction.  We place the highest importance on customer service after the sale and our rating with the Fair Trade Bureau of Arkansas shows it.  We're starting out 7th year, recently relocated. Satisfied Clients bring their family members, friends and co-workers to buy their cars, SUV's and trucks from MRAS.
You buy here / you pay here, Lending program opportunities too, Great Cash Prices
Finance with Flexibility we look at each individual uniquely and not a credit score
I think of my kids when getting our vehicles ready and your safety when you drive away in a MRAS car. . .  Drive away with Peace of Mind...
Maroon, Black and Silver colors.

Updates
I sent a response to the designers - have  not heard from them, will I receive my funds back?

Thank you all,  a lot of great designs - Making my decision on Nov 4th

So much talent. . .
So very challenging. . .
Thank you for your participation.
Sincerely,
Maple Ridge Auto Sales
Lorna Pettigrew

Industry/Entity Type
Safety
Contact Information for Business Card
Maple Ridge Auto Sales
"A Solid Car for a Solid Price"
4153 Oakvale Rd. North Little Rock, Ar 72118
Lorna Pettigrew
501.739.2018

```html
<!DOCTYPE html>
<html lang="en">
<head>
<meta charset="utf-8">
<title>Maple Ridge Auto Sales – Business Card</title>
<link rel="stylesheet" href="https://fonts.googleapis.com/css2?family=Yanone+Kaffeesatz:wght@300&family=Allura&display=swap">
<style>
  :root {
    --backdrop: #f0e9df;
    --maroon: #6b0a0a;
    --title-rust: #7e3527;
    --silver: #b9b6b4;
  }
  html, body {
    margin: 0;
    padding: 0;
    width: 1200px;
    height: 1200px;
    overflow: hidden;
    background: var(--backdrop);
  }
  .canvas {
    position: relative;
    width: 1200px;
    height: 1200px;
  }
  .business-card {
    position: absolute;
    left: 48px;
    top: 273px;
    width: 1085px;
    height: 635px;
    background: var(--maroon);
    text-align: center;
  }
  .company-name {
    position: absolute;
    left: 0;
    right: 0;
    top: 58px;
    margin: 0;
    font-family: "Yanone Kaffeesatz", "Arial Narrow", sans-serif;
    font-weight: 300;
    font-size: 112px;
    line-height: 1;
    color: var(--title-rust);
    letter-spacing: 1px;
  }
  .tagline {
    position: absolute;
    left: 0;
    right: 0;
    margin: 0;
    font-family: "Allura", cursive;
    color: var(--silver);
    line-height: 1;
    white-space: pre;
  }
  .tagline--payment {
    top: 278px;
    font-size: 76px;
  }
  .tagline--promise {
    top: 438px;
    font-size: 80px;
  }
</style>
</head>
<body>
  <main class="canvas">
    <section class="business-card">
      <h1 class="company-name">Maple Ridge Auto Sales</h1>
      <p class="tagline tagline--payment">You buy here!    You pay here!</p>
      <p class="tagline tagline--promise">Drive away with Peace of Mind...</p>
    </section>
  </main>
</body>
</html>
```